fernbolt website

commerce website to sell cookeries, brackets, mailboxes and to show off homes built. Modern Steel in design see kelvo rides web page to be like: https://www.kelvorides.com/en/ sorry its blue mantis hosting word press divi

must be able to add products to page

Target Market(s)

mainly western states of U.S.

Industry/Entity Type

Building Product

Coding

Coded - Design and coding required

Number of Pages Required

3 page

Font styles to use
Sans Serif

Colors

Designer to choose colors to be used in the design.

Requirements
Must have
• customers to be able to order products from page
• blue mantis hosting word press divi

```html
<!DOCTYPE html>
<html lang="en">
<head>
<meta charset="utf-8">
<title>Fernbolt Steel</title>
<link href="https://fonts.googleapis.com/css2?family=Poppins:wght@600;700&family=Lato:wght@400;700&display=swap" rel="stylesheet">
<style>
:root{
  --brand:#4a6592;
  --brand-dark:#3d5a8a;
  --ink:#1e1e22;
  --text:#333;
  --card:#ececec;
  --hero:#18191c;
  --footer:#2a2b2f;
  --white:#fff;
}
*{box-sizing:border-box;margin:0;padding:0}
html,body{width:1200px;height:3380px;overflow:hidden}
body{position:relative;font-family:'Lato',sans-serif;color:var(--text);background:var(--white)}
.abs{position:absolute}
.heading{font-family:'Poppins',sans-serif;font-weight:700;color:var(--brand-dark);text-transform:uppercase;letter-spacing:-.5px}
.btn{position:absolute;display:flex;align-items:center;justify-content:center;background:var(--brand);color:var(--white);font-size:11px;font-weight:700;border-radius:2px}

/* nav */
.nav{position:absolute;left:0;top:0;width:1200px;height:66px;background:var(--brand);z-index:3}
.nav a{position:absolute;top:26px;color:var(--white);font-size:12px;text-decoration:none}
.nav-badge{position:absolute;left:545px;top:0;width:110px;height:90px;border-radius:0 0 55px 55px;background:var(--brand);z-index:3;display:flex;align-items:center;justify-content:center;padding-top:4px}
.brandmark{font-family:'Lato',sans-serif;font-weight:700;color:var(--white);font-size:15px;letter-spacing:1px}

/* hero */
.hero{left:0;top:66px;width:1200px;height:407px;background:radial-gradient(ellipse at 70% 50%,#2c2d31,var(--hero) 70%)}
.hero-title{left:249px;top:186px;font-family:'Poppins',sans-serif;font-weight:700;font-size:30px;line-height:34px;color:var(--white)}
.hero-title span{color:#6f8dbd}
.hero-text{left:249px;top:258px;width:300px;font-size:16px;line-height:21px;color:#eee}
.hero-product{left:565px;top:144px;width:452px;height:394px;border-radius:50% 50% 30% 30%;background:radial-gradient(ellipse at 50% 40%,#9a9da3,#55585e 55%,rgba(40,40,44,0) 72%);z-index:2}

/* feature tiles */
.tile{top:583px;width:360px;height:289px;display:flex;align-items:flex-end;padding:0 22px 30px}
.tile p{color:var(--white);font-weight:700;font-size:17px;line-height:23px}

/* about */
.about{left:0;top:947px;width:1200px;height:359px;background:linear-gradient(90deg,#dcdde0,#ececee 40%,#f3f3f4)}
.about-photo{left:0;top:0;width:420px;height:359px;background:linear-gradient(90deg,#c9cacd,rgba(236,236,238,0))}
.about h2{position:absolute;left:0;width:1200px;top:55px;text-align:center;font-size:28px}
.about h3{position:absolute;left:0;width:1200px;top:102px;text-align:center;font-size:15px;font-weight:700;color:var(--ink)}
.about-copy{left:249px;top:138px;width:702px;text-align:center;font-size:11px;line-height:17px;color:#444}

/* products */
.products{left:0;top:1306px;width:1200px;height:708px;background:linear-gradient(100deg,#fff 55%,#e7e8ea)}
.section-title{position:absolute;left:0;width:1200px;text-align:center;font-size:28px}
.card{position:absolute;background:var(--card)}
.card .thumb{position:absolute;left:50%;transform:translateX(-50%);border-radius:50% 50% 35% 35%;background:radial-gradient(ellipse at 50% 35%,#6a6660,#3d3a36 60%,#8a847a)}
.card .name{position:absolute;left:13px;font-weight:700;color:var(--ink)}
.card .desc{position:absolute;left:13px;color:#444}
.card .price{position:absolute;left:13px;font-weight:700;color:var(--brand-dark)}
.card-sm{width:162px;height:242px}
.card-sm .thumb{top:30px;width:140px;height:112px}
.card-sm .name{top:165px;font-size:11px}
.card-sm .desc{top:185px;font-size:9.5px}
.card-sm .price{top:204px;font-size:11px}
.card-lg{top:2547px;width:214px;height:305px}
.card-lg .thumb{top:45px;width:170px;height:130px}
.card-lg .name{left:18px;top:206px;font-size:14px}
.card-lg .desc{left:18px;top:229px;font-size:11.5px}
.card-lg .price{left:18px;top:252px;font-size:15px}

/* who we are */
.who-photo{left:0;top:2014px;width:600px;height:425px;background:linear-gradient(180deg,#3f5a3c,#5a6a55 45%,#9b8a78 75%,#7d6f62)}
.who{left:600px;top:2014px;width:600px;height:425px;background:var(--brand);color:var(--white)}
.who h2{position:absolute;left:52px;top:52px;font-family:'Poppins',sans-serif;font-weight:700;font-size:26px}
.who h3{position:absolute;left:54px;top:96px;width:300px;font-size:15px;font-weight:700;line-height:21px}
.who p{position:absolute;left:54px;top:152px;width:295px;font-size:11px;line-height:17.2px}
.who .btn{left:55px;top:362px;width:91px;height:28px;background:var(--white);color:var(--brand)}

.arrow{position:absolute;top:2676px;width:26px;height:30px}

/* footer */
.footer-cap{left:470px;top:2908px;width:260px;height:200px;border-radius:50%;background:var(--footer)}
.footer{left:0;top:3007px;width:1200px;height:373px;background:var(--footer);color:#ccc}
.footer .brandmark{position:absolute;left:0;width:1200px;top:35px;text-align:center;font-size:26px;font-weight:400;letter-spacing:1px}
.footer h4{position:absolute;top:113px;color:#7f9ccd;font-size:11px;font-weight:700}
.footer .col{position:absolute;font-size:9px;line-height:14px;color:#ddd}
.footer ul{list-style:none}
.footer li{margin-bottom:13px;font-size:9px}
.footer li::before{content:"•";margin-right:8px}
.news-item{display:flex;gap:14px;margin-bottom:12px}
.news-thumb{width:46px;height:42px;flex:none;background:linear-gradient(180deg,#6b7f8e,#8a6c52)}
.contact-label{font-size:12px;font-weight:700;color:var(--white)}
.copyright{left:249px;top:3347px;font-size:9px;color:#ddd}
.copyright span{color:#7f9ccd}
.social{top:3344px;width:18px;height:18px;border-radius:50%;background:#e8e8e8}
</style>
</head>
<body>

<nav class="nav">
  <a style="left:249px">Home</a>
  <a style="left:315px">About us</a>
  <a style="left:400px">Product</a>
  <a style="left:730px">Who we are</a>
  <a style="left:827px">Contact.</a>
  <a style="left:903px;font-size:9px;top:28px">
    <svg width="11" height="10" viewBox="0 0 11 10" style="vertical-align:-1px"><path d="M0 1h2l1.5 5h6L11 2.5H3" fill="none" stroke="#fff" stroke-width="1.3"/><circle cx="4.5" cy="8.5" r="1" fill="#fff"/><circle cx="8.5" cy="8.5" r="1" fill="#fff"/></svg>
    (0) Item</a>
</nav>
<div class="nav-badge"><span class="brandmark">FERNBOLT</span></div>

<section class="abs hero"></section>
<h1 class="abs hero-title"><span>FERNBOLT</span> OUTDOOR<br>FIREPIT COOKERY</h1>
<p class="abs hero-text">Lorem Ipsum is simply dummy text of the printing and typesetting industry.</p>
<span class="btn" style="left:249px;top:322px;width:91px;height:27px">Contact us</span>
<div class="abs hero-product" role="img" aria-label="Steel fire pit with mesh dome lid and firewood"></div>

<div class="abs tile" style="left:42px;background:linear-gradient(160deg,#4a3a30,#b4501c 55%,#2a1c15)" role="img" aria-label="Glowing coals behind a steel grill grate"><p>Lorem Ipsum is simply dummy text of theprinting and typesetting</p></div>
<div class="abs tile" style="left:425px;background:linear-gradient(180deg,#1c3e7a,#2a4f8a 45%,#3a2a22)" role="img" aria-label="Friends gathered around a fire pit at dusk"><p>Lorem Ipsum is simply dummy text of theprinting and typesetting</p></div>
<div class="abs tile" style="left:809px;background:linear-gradient(180deg,#6d7a5c,#9a958c 50%,#4a4440)" role="img" aria-label="Stone fire pit ringed by white patio chairs"><p>Lorem Ipsum is simply dummy text of theprinting and typesetting</p></div>

<section class="abs about">
  <div class="abs about-photo" role="img" aria-label="Faded stone patio fire pit"></div>
  <h2 class="heading">About us</h2>
  <h3>Lorem Ipsum is simply dummy text of theprinting and typesetting industry.</h3>
  <p class="abs about-copy">Lorem Ipsum is simply dummy text of the printing and typesetting industry. Lorem Ipsum has been the industry's standard dummy text ever since the 1500s, when an unknown printer took a galley of type and scrambled it to make a type specimen book. It has survived not only five centuries, but also the leap into electronic typesetting, remaining essentially unchanged. It was popularised in the 1960s with the release of Letraset sheets containing Lorem Ipsum passages, and more recently with desktop publishing software like Aldus PageMaker including versions of Lorem Ipsum. Lorem Ipsum is simply dummy text of the printing and typesetting industry. Lorem Ipsum has been the industry's standard dummy text ever since the 1500s, when an unknown printer took a galley of type and scrambled it to make a type specimen book. It has survived not only five</p>
  <span class="btn" style="left:561px;top:284px;width:90px;height:28px">Read More</span>
</section>

<section class="abs products">
  <h2 class="heading section-title" style="top:34px">Our Products</h2>
</section>

<div class="card card-sm" style="left:249px;top:1407px"><div class="thumb" role="img" aria-label="Bronze steel fire pit"></div><span class="name">Fernbolt Product 1</span><span class="desc">Lorem Ipsum is simply dummy</span><span class="price">$125.00</span></div>
<div class="card card-sm" style="left:429px;top:1407px"><div class="thumb" role="img" aria-label="Bronze steel fire pit"></div><span class="name">Fernbolt Product 1</span><span class="desc">Lorem Ipsum is simply dummy</span><span class="price">$125.00</span></div>
<div class="card card-sm" style="left:609px;top:1407px"><div class="thumb" role="img" aria-label="Bronze steel fire pit"></div><span class="name">Fernbolt Product 1</span><span class="desc">Lorem Ipsum is simply dummy</span><span class="price">$125.00</span></div>
<div class="card card-sm" style="left:789px;top:1407px"><div class="thumb" role="img" aria-label="Bronze steel fire pit"></div><span class="name">Fernbolt Product 1</span><span class="desc">Lorem Ipsum is simply dummy</span><span class="price">$125.00</span></div>
<div class="card card-sm" style="left:249px;top:1673px"><div class="thumb" role="img" aria-label="Bronze steel fire pit"></div><span class="name">Fernbolt Product 1</span><span class="desc">Lorem Ipsum is simply dummy</span><span class="price">$125.00</span></div>
<div class="card card-sm" style="left:429px;top:1673px"><div class="thumb" role="img" aria-label="Bronze steel fire pit"></div><span class="name">Fernbolt Product 1</span><span class="desc">Lorem Ipsum is simply dummy</span><span class="price">$125.00</span></div>
<div class="card card-sm" style="left:609px;top:1673px"><div class="thumb" role="img" aria-label="Bronze steel fire pit"></div><span class="name">Fernbolt Product 1</span><span class="desc">Lorem Ipsum is simply dummy</span><span class="price">$125.00</span></div>
<div class="card card-sm" style="left:789px;top:1673px"><div class="thumb" role="img" aria-label="Bronze steel fire pit"></div><span class="name">Fernbolt Product 1</span><span class="desc">Lorem Ipsum is simply dummy</span><span class="price">$125.00</span></div>
<span class="btn" style="left:554px;top:1952px;width:92px;height:28px">View More</span>

<div class="abs who-photo" role="img" aria-label="Backyard patio with curved stone seating wall, fire pit and pavilion among pines"></div>
<section class="abs who">
  <h2>WHO WE ARE</h2>
  <h3>Lorem Ipsum is simply dummy text of the printing and typesetting industry.</h3>
  <p>Lorem Ipsum is simply dummy text of the printing and typesetting industry. Lorem Ipsum has been the industry's standard dummy text ever since the 1500s, when an unknown printer took a galley of type and scrambled it to make a type specimen book. It has survived not only five centuries, but also the leap into electronic typesetting, remaining essentially unchanged. It was popularised in the 1960s with the release of Letraset sheets containing Lorem Ipsum passages, and more recently with desktop publishing software like Aldus PageMaker including versions of Lorem Ipsum.</p>
  <span class="btn">Read More</span>
</section>

<h2 class="heading section-title" style="top:2478px">Featured Product</h2>
<svg class="arrow" style="left:195px" viewBox="0 0 26 30"><path d="M18 4 7 15l11 11" fill="none" stroke="#222" stroke-width="3"/></svg>
<svg class="arrow" style="left:987px" viewBox="0 0 26 30"><path d="M8 4l11 11L8 26" fill="none" stroke="#222" stroke-width="3"/></svg>
<div class="card card-lg" style="left:249px"><div class="thumb" role="img" aria-label="Bronze steel fire pit"></div><span class="name">Fernbolt Product 1</span><span class="desc">Lorem Ipsum is simply dummy</span><span class="price">$125.00</span></div>
<div class="card card-lg" style="left:494px"><div class="thumb" role="img" aria-label="Bronze steel fire pit"></div><span class="name">Fernbolt Product 1</span><span class="desc">Lorem Ipsum is simply dummy</span><span class="price">$125.00</span></div>
<div class="card card-lg" style="left:737px"><div class="thumb" role="img" aria-label="Bronze steel fire pit"></div><span class="name">Fernbolt Product 1</span><span class="desc">Lorem Ipsum is simply dummy</span><span class="price">$125.00</span></div>

<div class="abs footer-cap"></div>
<footer class="abs footer">
  <span class="brandmark">FERNBOLT</span>
  <h4 style="left:249px">About us</h4>
  <p class="col" style="left:249px;top:152px;width:165px">Lorem Ipsum is simply dummy text of the printing and typesetting industry. Lorem Ipsum has been the industry's standard dummy text ever since the 1500s, when an unknown printer took a galley of type and scrambled it to make a type specimen book. It has survived not only five centuries, but also the leap into remaining essentially unchanged. It was popularised in</p>
  <h4 style="left:442px">My Account</h4>
  <ul class="col" style="left:442px;top:155px"><li>Wishlist</li><li>My Account</li><li>Checkout</li><li>Cart</li></ul>
  <h4 style="left:550px">News</h4>
  <div class="col" style="left:553px;top:153px;width:170px">
    <div class="news-item"><div class="news-thumb" role="img" aria-label="Patio fire pit"></div><span>Lorem Ipsum is simply dummy text of the printing and typesetting industry. Lorem Ipsum has</span></div>
    <div class="news-item"><div class="news-thumb" role="img" aria-label="Stone fire pit"></div><span>Lorem Ipsum is simply dummy text of the printing and typesetting industry. Lorem Ipsum has</span></div>
  </div>
  <h4 style="left:796px">Contact us</h4>
  <div class="col" style="left:800px;top:155px;width:160px">
    <svg width="10" height="13" viewBox="0 0 10 13" style="position:absolute;left:0;top:2px"><path d="M5 12S1 7 1 4.5a4 4 0 0 1 8 0C9 7 5 12 5 12z" fill="none" stroke="#7f9ccd" stroke-width="1.4"/><circle cx="5" cy="4.5" r="1.3" fill="#7f9ccd"/></svg>
    <div style="padding-left:22px"><span class="contact-label">Address:</span><p style="margin-top:12px">Abc Street City #12345 simply dummy text of the printing and typesetting</p></div>
    <svg width="11" height="11" viewBox="0 0 11 11" style="position:absolute;left:0;top:89px"><path d="M2 1l2 2-1 1.5c.8 1.5 2 2.7 3.5 3.5L8 7l2 2-1.5 1.5C5 10 1 6 .5 2.5z" fill="#7f9ccd"/></svg>
    <div style="padding-left:22px;margin-top:12px"><span class="contact-label">Phone:</span><p style="margin-top:3px">(123)456-6789</p></div>
  </div>
</footer>
<p class="abs copyright">Copyright 2020 <span>Fernbolt Steel</span> All Right Reserved.</p>
<span class="abs social" style="left:853px"></span>
<span class="abs social" style="left:880px"></span>
<span class="abs social" style="left:906px"></span>
<span class="abs social" style="left:932px"></span>

</body>
</html>
```